Robotic startup business cards

We are looking for a design for a set of business cards which reflect the spirit and humor of Vortalo Robotics. We want to present ourselves as sleek, professional, but laid-back consulting company.

We primarily focus on developing robotic arms software. This software controls robots and does things like grab items, pick objects up, move them, etc.

We want to allow you maximum design creativity, but do ask that you consider our existing style guidelines (see attached files) in order to make our brand cohesive.

Target Market(s)

Startups and Mid-size robotic companies

Industry/Entity Type

Business

Contact Information for Business Card

Miro Halvensky, PhD
Roboticist | Vortalo Consulting | 318.570.9164

Font styles to use
Other font styles liked:
• Source code pro

Requirements
Must have
• robots or robotic arms
• similar color scheme that works with existing brand guidelines
Nice to have
• please consider our existing style guidelines (see attached files) in order to make our brand cohesive.
• minimalism style is generally nice.
Should not have
• An old, boring, or corporate feel. Too much text.

```html
<!DOCTYPE html>
<html lang="en">
<head>
<meta charset="utf-8">
<title>Vortalo Consulting – Business Cards</title>
<link rel="stylesheet" href="https://fonts.googleapis.com/css2?family=Source+Code+Pro:wght@400;500;600&family=Work+Sans:wght@400&display=swap">
<style>
  :root {
    --bg: #141414;
    --card: #232323;
    --card-light: #2f2f2f;
    --green: #5cc495;
    --white: #f2f2f2;
  }
  * { margin: 0; padding: 0; box-sizing: border-box; }
  html, body { width: 1200px; height: 897px; overflow: hidden; background: var(--bg); }
  .canvas { position: relative; width: 1200px; height: 897px; }
  .card {
    position: absolute; left: 304px; width: 594px; height: 338px;
    border-radius: 18px;
    background: linear-gradient(135deg, var(--card) 45%, var(--card-light) 100%);
  }
  .card--front { top: 92px; }
  .card--back { top: 470px; }

  .brand-mark {
    position: absolute; display: flex; align-items: center; gap: 12px;
    font-family: "Source Code Pro", monospace; font-weight: 500; color: var(--green);
  }
  .brand-mark .dot { border-radius: 50%; background: var(--green); flex: none; }
  .card--front .brand-mark { left: 66px; top: 148px; font-size: 26px; letter-spacing: 2px; }
  .card--front .brand-mark .dot { width: 22px; height: 22px; }

  .contact { position: absolute; left: 300px; top: 82px; }
  .contact .name {
    font-family: "Source Code Pro", monospace; font-size: 20px; letter-spacing: 1.5px;
    color: var(--green); font-weight: 400; line-height: 1;
  }
  .contact .role, .contact .address, .contact .line {
    font-family: "Work Sans", sans-serif; font-size: 13.5px; color: var(--white);
  }
  .contact .role { margin-top: 8px; }
  .contact .company {
    margin-top: 16px; font-family: "Source Code Pro", monospace; font-weight: 600;
    font-size: 13px; letter-spacing: 1px; color: var(--green);
  }
  .contact .address { line-height: 17px; margin-top: 2px; }
  .contact .lines { margin-top: 10px; list-style: none; }
  .contact .line { display: flex; align-items: center; gap: 8px; height: 19.5px; }
  .contact .line svg { width: 11px; height: 11px; flex: none; }

  .card--back .brand-mark {
    left: 0; right: 0; top: 128px; justify-content: center; gap: 22px;
    color: var(--white); font-size: 58px; font-weight: 400; letter-spacing: 8px;
  }
  .card--back .brand-mark .dot { width: 40px; height: 40px; }
  .web {
    position: absolute; left: 0; right: 0; top: 288px; text-align: center;
    font-family: "Work Sans", sans-serif; font-size: 16px; letter-spacing: 2px; color: var(--white);
  }
  .web .accent { color: var(--green); }
</style>
</head>
<body>
<main class="canvas">
  <section class="card card--front">
    <div class="brand-mark"><span class="dot"></span>VORTALO</div>
    <div class="contact">
      <h1 class="name">Miro Halvensky, PhD</h1>
      <p class="role">Roboticist</p>
      <p class="company">VORTALO CONSULTING</p>
      <p class="address">2047 Korvel, Lindamar<br>str. 18/B, Estoria</p>
      <ul class="lines">
        <li class="line">
          <svg viewBox="0 0 12 12"><path fill="#5cc495" d="M2.4 0.6l2 2.2-1 1.4c.7 1.6 2 2.9 3.6 3.6l1.4-1 2.2 2-1.1 2.2C5 10.8 1.2 7 0.2 1.7z"/></svg>
          318.570.9164
        </li>
        <li class="line">
          <svg viewBox="0 0 12 12"><rect x="0.5" y="2" width="11" height="8" fill="#5cc495"/><path d="M0.5 2.5L6 6.8 11.5 2.5" fill="none" stroke="#232323" stroke-width="1"/></svg>
          info@vortaloconsulting.com
        </li>
        <li class="line">
          <svg viewBox="0 0 12 12" fill="none" stroke="#5cc495" stroke-width="0.9"><circle cx="6" cy="6" r="5.3"/><ellipse cx="6" cy="6" rx="2.3" ry="5.3"/><path d="M0.7 6h10.6M1.6 3.3h8.8M1.6 8.7h8.8"/></svg>
          www.vortaloconsulting.com
        </li>
      </ul>
    </div>
  </section>

  <section class="card card--back">
    <div class="brand-mark"><span class="dot"></span>VORTALO</div>
    <p class="web">www.<span class="accent">vortaloconsulting</span>.com</p>
  </section>
</main>
</body>
</html>
```